Website Design - for Energy Efficiency company - large corporate feel

Hi there,
Thanks for checking out this project!
We're a UK based energy efficiency business. We arrange for energy efficient systems to be fitted in people's houses (i.e. efficient boilers, solar panels etc.) However, we do not install them ourselves as we have accredited installers who install on our behalf. Therefore the website should appeal to these businesses and have a very professional corporate feel. The final design should communicate that we are a financially safe large corporation.
Our existing website should not be used for inspiration as the style and content are very outdated (it was from a time when were installers - which we no longer are).
The new website design should use the greens from our logo, however I don't want the site saturated in this colour.
I'm really open to your chosen layout and therefore I'm not a huge fan of including links to websites I like - as I don't want to limit your own creativity. However, I would like it to look corporate (but not too boring and unimaginative).
So here's a few links to websites that I feel give a feel of financially safe / large corporate etc. Although you certainly don't have to design with this style / layout in mind:
http://www.brelvanhub.org.uk/advice
http://www.tolvenrise.co.uk/
http://www.qpwd.org.uk/
http://www.wendrowkeyplot.co.uk/
http://www.ruvasto.co.uk/ (very bad design but looks corporate)
http://www.pellarwatt.org.uk/
http://www.vq.co.uk/ (looks corporate but too busy and boring)
http://www.quellisto.co.uk/business/index.htm
http://www.dormavel.com/
https://www.ostrevan.com/en/index.html
The site is for 4 different audiences:
Consumers | Businesses | Public Sector | Installers
Therefore, it's important that there is some form of way of splitting the site up into these sections (almost like 4 websites in 1). Each section will then have the navigation menu with 7 links.
I've attached our logo (company-logo.jpg) and another logo design we have to display inline with regulations (blue-pact-logo.jpg).
Happy designing, and thank you!

```html
<!DOCTYPE html>
<html lang="en">
<head>
<meta charset="utf-8">
<title>Verdalo Energy</title>
<link rel="stylesheet" href="https://fonts.googleapis.com/css2?family=Arimo:wght@400;700&display=swap">
<style>
  :root {
    --green: #5a9a1f;
    --green-dark: #3f7d12;
    --green-bright: #8cc63f;
    --ink: #1f1f1f;
    --nav-ink: #3a3a3a;
    --header-grey: #efefef;
    --band-grey: #d9d9d9;
    --footer-grey: #ececec;
    --rule: #bdbdbd;
    --white: #ffffff;
  }
  * { box-sizing: border-box; margin: 0; padding: 0; }
  html, body { width: 1080px; height: 1200px; overflow: hidden; background: var(--white); }
  body { position: relative; font-family: "Arimo", Arial, sans-serif; color: var(--ink); }

  .site-header { position: absolute; left: 0; top: 0; width: 1080px; height: 102px; background: var(--header-grey); }
  .brand-panel { position: absolute; left: 0; top: 0; }
  .brand { position: absolute; left: 100px; top: 33px; display: flex; align-items: center; gap: 8px;
    font-size: 20px; font-weight: 700; color: var(--green); letter-spacing: 0.3px; white-space: nowrap; }
  .brand-dot { width: 32px; height: 32px; border-radius: 50%; background: var(--green); flex: none; }

  .main-nav { position: absolute; left: 384px; top: 37px; display: flex; list-style: none; }
  .main-nav li { font-size: 15px; color: var(--nav-ink); padding: 6px 14px; margin-right: 14px; white-space: nowrap; }
  .main-nav li.is-active { background: var(--green-bright); color: var(--white); border-radius: 2px; }

  .hero { position: absolute; left: 0; top: 102px; width: 1080px; height: 460px;
    background: linear-gradient(180deg, #3f6fc4 0%, #9fb9e0 28%, #e6eef8 45%, #8aa3b8 58%, #3e7a2a 72%, #6cbf2e 86%, #9ad94a 100%); }
  .hero-cta { position: absolute; left: 418px; top: 512px; width: 244px; height: 50px;
    background: rgba(215, 240, 190, 0.75); border-radius: 8px 8px 0 0;
    font-size: 17px; color: #333; letter-spacing: 0.5px; text-align: center; line-height: 52px; }

  .intro-band { position: absolute; left: 0; top: 562px; width: 1080px; height: 80px; background: var(--band-grey);
    box-shadow: 0 2px 3px rgba(0,0,0,0.15); }
  .intro-title { position: absolute; left: 130px; top: 22px; font-size: 27px; font-weight: 400; color: var(--green); letter-spacing: 0.5px; }
  .intro-text { position: absolute; left: 385px; top: 20px; font-size: 13px; line-height: 20px; color: #222; white-space: nowrap; }

  .audience-rule-v { position: absolute; left: 532px; top: 692px; width: 1px; height: 366px; background: var(--rule); }
  .audience-rule-h { position: absolute; left: 121px; top: 876px; width: 825px; height: 1px; background: var(--rule); }

  .audience { position: absolute; width: 400px; height: 160px; }
  .audience-photo { position: absolute; left: 0; top: 0; width: 144px; height: 144px; border-radius: 50%; }
  .audience-title { position: absolute; left: 166px; top: 14px; font-size: 19px; font-weight: 400; color: var(--green); letter-spacing: 0.5px; white-space: nowrap; }
  .audience-text { position: absolute; left: 166px; top: 42px; font-size: 13.5px; line-height: 18px; color: #222; white-space: nowrap; }
  .read-more { position: absolute; left: 166px; top: 127px; width: 139px; height: 27px; border: 1px solid var(--green-dark);
    font-size: 13.5px; color: #222; text-align: center; line-height: 25px; }

  .audience--consumers { left: 122px; top: 684px; }
  .audience--businesses { left: 588px; top: 684px; }
  .audience--public { left: 122px; top: 902px; }
  .audience--installers { left: 589px; top: 902px; }
  .audience--public .audience-title, .audience--installers .audience-title { top: 9px; }
  .audience--public .audience-text, .audience--installers .audience-text { top: 39px; }
  .audience--public .read-more, .audience--installers .read-more { top: 118px; left: 167px; }

  .photo-people { background: radial-gradient(circle at 50% 45%, #e0c8b0, #a7806a 60%, #6b4c3e); }
  .photo-handshake { background: linear-gradient(135deg, #b9c1c6, #6e777c 55%, #2b2f33); }
  .photo-crowd { background: radial-gradient(circle at 50% 40%, #b08e78, #5b4538 60%, #2a2220); }
  .photo-roof { background: linear-gradient(180deg, #6f9fd8 0%, #9cc0e8 30%, #4a5560 55%, #2f3338 100%); }

  .site-footer { position: absolute; left: 0; top: 1108px; width: 1080px; height: 92px; background: var(--footer-grey);
    border-top: 2px solid #d3d3d3; }
  .footer-nav { position: absolute; left: 108px; top: 41px; display: flex; list-style: none; }
  .footer-nav li { font-size: 13px; color: #333; margin-right: 41px; white-space: nowrap; }
  .social { position: absolute; top: 37px; width: 26px; height: 26px; border-radius: 2px; }
  .social--one { left: 805px; background: #3b5998; }
  .social--two { left: 839px; background: #1f7bb6; }
  .social--three { left: 872px; background: #2aa3e6; }
  .approval-badge { position: absolute; left: 913px; top: 10px; width: 52px; height: 76px; }
</style>
</head>
<body>
  <header class="site-header">
    <svg class="brand-panel" width="362" height="102" viewBox="0 0 362 102" aria-hidden="true">
      <polygon points="0,0 314,0 360,102 0,102" fill="#ffffff"/>
    </svg>
    <div class="brand"><span class="brand-dot"></span>VERDALO ENERGY</div>
    <ul class="main-nav">
      <li class="is-active">home</li>
      <li>about us</li>
      <li>consumers</li>
      <li>businesses</li>
      <li>public sectors</li>
      <li>installers</li>
    </ul>
  </header>

  <div class="hero" role="img" aria-label="City skyscrapers rising from a green grassy hill with trees under a bright blue sky with clouds"></div>
  <div class="hero-cta">CONTACT US</div>

  <section class="intro-band">
    <h1 class="intro-title">Verdalo Energy</h1>
    <p class="intro-text">Typi non habent claritatem insitam; est usus legentis in iis qui facit eorum claritatem. Investiga-<br>tiones demonstraverunt lectores legere me lius quod ii legunt saepius. Claritas est etiam pro</p>
  </section>

  <div class="audience-rule-v"></div>
  <div class="audience-rule-h"></div>

  <article class="audience audience--consumers">
    <div class="audience-photo photo-people" role="img" aria-label="Group of smiling people of different ages"></div>
    <h2 class="audience-title">Consumers</h2>
    <p class="audience-text">Lorem ipsum dolor sit amet,<br>consectetuer adipiscing elit, sed<br>diam nonummy nibh euismod<br>tinci volutpat adipisci</p>
    <div class="read-more">Read more</div>
  </article>

  <article class="audience audience--businesses">
    <div class="audience-photo photo-handshake" role="img" aria-label="Business people shaking hands seen from above"></div>
    <h2 class="audience-title">Businesses</h2>
    <p class="audience-text">Lorem ipsum dolor sit amet,<br>consectetuer adipiscing elit, sed<br>diam nonummy nibh euismod<br>tinci volutpat adipisci</p>
    <div class="read-more">Read more</div>
  </article>

  <article class="audience audience--public">
    <div class="audience-photo photo-crowd" role="img" aria-label="Crowd of people in a public space"></div>
    <h2 class="audience-title">Public Sectors</h2>
    <p class="audience-text">Lorem ipsum dolor sit amet,<br>consectetuer adipiscing elit, sed<br>diam nonummy nibh euismod<br>tinci volutpat adipisci</p>
    <div class="read-more">Read more</div>
  </article>

  <article class="audience audience--installers">
    <div class="audience-photo photo-roof" role="img" aria-label="Installers fitting solar panels on a roof"></div>
    <h2 class="audience-title">Installers</h2>
    <p class="audience-text">Lorem ipsum dolor sit amet,<br>consectetuer adipiscing elit, sed<br>diam nonummy nibh euismod<br>tinci volutpat adipisci</p>
    <div class="read-more">Read more</div>
  </article>

  <footer class="site-footer">
    <ul class="footer-nav">
      <li>home</li>
      <li>about us</li>
      <li>consumers</li>
      <li>businesses</li>
      <li>public sectors</li>
      <li>installers</li>
    </ul>
    <div class="social social--one" role="img" aria-label="Social network link"></div>
    <div class="social social--two" role="img" aria-label="Social network link"></div>
    <div class="social social--three" role="img" aria-label="Social network link"></div>
    <svg class="approval-badge" viewBox="0 0 52 76" role="img" aria-label="Regulatory approval badge">
      <rect x="8" y="6" width="36" height="56" fill="#2f7a1a"/>
    </svg>
  </footer>
</body>
</html>
```